Country House in Italy Needs a Business Card Design

We need a business card design for “Casale del Ginepro”, a modern concept of a Farm Holidays/Country House to be opened in central Italy.
Attached is the company logo you did for us in the past.
Please
- create a double-sided business card design
- on the back I would like to have the logo
- on the front the copy
Copy on card:
o Casale del Ginepro
o Address: Via Pontemurra, 14
Cingoli (MC), Italy
o Website: www.casaledelginepro.it
o Email: info@casaledelginepro.it
o my name : Marisa
o my mobile phone number: +39 347 8123905
In the distribution of information keep in mind the possible inclusion also of a landline telephone number (currently not available / existing).
WE WOULD LIKE TO HAVE A MODERN, PROFFESIONAL, OUT OF THE BOX BUSINESS CARD. BE AS CREATIVE AS YOU WOULD LIKE.

```html
<!DOCTYPE html>
<html lang="it">
<head>
<meta charset="utf-8">
<title>Casale del Ginepro – Biglietto da visita</title>
<link rel="stylesheet" href="https://fonts.googleapis.com/css2?family=Cormorant+Garamond:wght@500;600&family=Marcellus&display=swap">
<style>
  :root {
    --backdrop: #e7e4df;
    --card: #ffffff;
    --card-shade: #f1f0ee;
    --gold-light: #e2c49b;
    --gold: #c89f6c;
    --gold-deep: #a97c4a;
    --orange: #e87a2c;
    --ink: #4a4038;
    --ink-soft: #7a6e64;
  }
  * { box-sizing: border-box; margin: 0; padding: 0; }
  html, body { width: 1200px; height: 900px; overflow: hidden; }
  body {
    background: var(--backdrop);
    font-family: "Cormorant Garamond", Georgia, serif;
    color: var(--ink);
    position: relative;
  }
  .card {
    position: absolute;
    left: 320px;
    width: 560px;
    height: 320px;
    border-radius: 34px;
    background: linear-gradient(135deg, var(--card) 55%, var(--card-shade));
    box-shadow: 0 10px 28px rgba(60, 45, 30, 0.18);
    overflow: hidden;
  }
  .card--front { top: 95px; }
  .card--back { top: 480px; }

  .gold-band { position: absolute; inset: 0; width: 100%; height: 100%; }

  .brand { position: absolute; display: flex; align-items: center; gap: 12px; }
  .brand-mark {
    width: 42px; height: 42px; border-radius: 50%;
    background: var(--orange);
    flex: none;
  }
  .brand-name {
    font-family: "Marcellus", Georgia, serif;
    font-size: 27px;
    color: var(--ink);
    line-height: 1;
    white-space: nowrap;
  }
  .brand-tagline {
    font-family: "Cormorant Garamond", Georgia, serif;
    font-size: 14px;
    font-weight: 600;
    letter-spacing: 2px;
    color: var(--orange);
    text-transform: uppercase;
    margin-top: 6px;
  }
  .card--front .brand { left: 34px; top: 128px; }

  .person { position: absolute; left: 40px; top: 214px; }
  .person-name {
    font-size: 22px; font-weight: 600; letter-spacing: 2px;
    text-transform: uppercase; color: var(--ink);
  }
  .person-role {
    font-size: 15px; font-weight: 600; letter-spacing: 2px;
    text-transform: uppercase; color: var(--ink-soft); margin-top: 2px;
  }

  .contacts { position: absolute; left: 345px; top: 146px; list-style: none; }
  .contact {
    display: flex; align-items: flex-start; gap: 8px;
    font-size: 13px; font-weight: 600; letter-spacing: 0.5px;
    line-height: 1.2; margin-bottom: 5px; color: var(--ink-soft);
    white-space: nowrap;
  }
  .contact-icon { width: 13px; height: 13px; flex: none; margin-top: 1px; }

  .card--back .brand {
    left: 50%; top: 50%; transform: translate(-50%, -50%);
  }
</style>
</head>
<body>

  <section class="card card--front" aria-label="Fronte del biglietto">
    <svg class="gold-band" viewBox="0 0 560 320" aria-hidden="true">
      <defs>
        <linearGradient id="goldFill" x1="0" y1="0" x2="1" y2="1">
          <stop offset="0" stop-color="var(--gold-light)"/>
          <stop offset="0.55" stop-color="var(--gold)"/>
          <stop offset="1" stop-color="var(--gold-deep)"/>
        </linearGradient>
      </defs>
      <path d="M0 0 L0 26 C120 34 250 108 400 110 C470 110 520 100 560 92 L560 0 Z" fill="url(#goldFill)"/>
      <path d="M60 22 C160 36 270 92 400 92 C470 92 520 80 560 70" fill="none" stroke="#ffffff" stroke-opacity="0.85" stroke-width="4"/>
    </svg>

    <div class="brand">
      <span class="brand-mark" aria-hidden="true"></span>
      <div>
        <div class="brand-name">Casale del Ginepro</div>
        <div class="brand-tagline">Country House</div>
      </div>
    </div>

    <div class="person">
      <div class="person-name">Marisa</div>
      <div class="person-role">Titolare</div>
    </div>

    <ul class="contacts">
      <li class="contact">
        <svg class="contact-icon" viewBox="0 0 14 14" aria-hidden="true"><circle cx="7" cy="7" r="7" fill="var(--orange)"/><path d="M7 3.2a2.3 2.3 0 0 0-2.3 2.3C4.7 7.3 7 10.6 7 10.6s2.3-3.3 2.3-5.1A2.3 2.3 0 0 0 7 3.2z" fill="#fff"/></svg>
        <span>Via Pontemurra, 14<br>Cingoli (MC), Italy</span>
      </li>
      <li class="contact">
        <svg class="contact-icon" viewBox="0 0 14 14" aria-hidden="true"><circle cx="7" cy="7" r="7" fill="var(--orange)"/><rect x="5" y="3" width="4" height="8" rx="1" fill="#fff"/></svg>
        <span>+39 347 8123905</span>
      </li>
      <li class="contact">
        <svg class="contact-icon" viewBox="0 0 14 14" aria-hidden="true"><circle cx="7" cy="7" r="7" fill="var(--orange)"/><path d="M4.2 3.6l1.5-.3.8 1.8-.9.7a5 5 0 0 0 2.6 2.6l.7-.9 1.8.8-.3 1.5C7 9.9 4 7 4.2 3.6z" fill="#fff"/></svg>
        <span>+39 0733 000000</span>
      </li>
      <li class="contact">
        <svg class="contact-icon" viewBox="0 0 14 14" aria-hidden="true"><circle cx="7" cy="7" r="7" fill="var(--orange)"/><path d="M4.2 3.6l1.5-.3.8 1.8-.9.7a5 5 0 0 0 2.6 2.6l.7-.9 1.8.8-.3 1.5C7 9.9 4 7 4.2 3.6z" fill="#fff"/></svg>
        <span>+39 0733 000001</span>
      </li>
      <li class="contact">
        <svg class="contact-icon" viewBox="0 0 14 14" aria-hidden="true"><circle cx="7" cy="7" r="7" fill="var(--orange)"/><rect x="3.5" y="4.5" width="7" height="5" fill="#fff"/><path d="M3.5 4.5 7 7.3l3.5-2.8" fill="none" stroke="var(--orange)" stroke-width="0.8"/></svg>
        <span>info@casaledelginepro.it</span>
      </li>
      <li class="contact">
        <svg class="contact-icon" viewBox="0 0 14 14" aria-hidden="true"><circle cx="7" cy="7" r="7" fill="var(--orange)"/><circle cx="7" cy="7" r="3.4" fill="none" stroke="#fff" stroke-width="1"/><path d="M3.6 7h6.8M7 3.6v6.8" stroke="#fff" stroke-width="0.8"/></svg>
        <span>www.casaledelginepro.it</span>
      </li>
    </ul>
  </section>

  <section class="card card--back" aria-label="Retro del biglietto">
    <div class="brand">
      <span class="brand-mark" aria-hidden="true"></span>
      <div>
        <div class="brand-name">Casale del Ginepro</div>
        <div class="brand-tagline">Country House</div>
      </div>
    </div>
  </section>

</body>
</html>
```